automotive repair and collision repair shop card

our company is called K.R Motor service we are a automotive repair company
we also do government inspections. the company information is on the cards. I would like you to use my new logo and create a new card and use the information from my old card. Good Luck!!

Industry/Entity Type

Car Repair

Contact Information for Business Card

Address: #417-15862 91 Ave, Surrey, BC V5T 8K4
Phone:(604) 555-0187
fax 604 555 0142
website www.krmotor.example

Font styles to use
Serif
Sans Serif

Requirements
Must have
• all the information
Should not have
• the owner and there name

```html
<!DOCTYPE html>
<html lang="en">
<head>
<meta charset="utf-8">
<title>K.R Motor service – Business Card</title>
<link rel="stylesheet" href="https://fonts.googleapis.com/css2?family=Arimo:wght@400;700&display=swap">
<style>
  :root {
    --backdrop: #ececec;
    --card: #262626;
    --ink: #e6e6e6;
    --ink-muted: #a9a9a9;
    --rule: #8a8a8a;
  }
  * { margin: 0; padding: 0; box-sizing: border-box; }
  html, body {
    width: 1200px; height: 800px; overflow: hidden;
    background: var(--backdrop);
    font-family: "Arimo", Arial, sans-serif;
  }
  .sheet {
    position: relative; width: 1200px; height: 800px;
    display: flex; align-items: center; justify-content: center; gap: 40px;
  }
  .card {
    position: relative; width: 540px; height: 309px;
    background: var(--card); color: var(--ink);
  }
  .brand {
    display: flex; align-items: center; gap: 12px;
    font-family: "Arimo", Arial, sans-serif; font-weight: 700;
    color: var(--ink); letter-spacing: 0.04em; text-transform: uppercase;
  }
  .brand-dot {
    width: 16px; height: 16px; border-radius: 50%; background: var(--ink);
  }
  .card-front .brand {
    position: absolute; left: 50%; top: 50%; transform: translate(-50%, -50%);
    font-size: 30px; white-space: nowrap;
  }
  .card-back .brand {
    position: absolute; left: 34px; top: 196px; font-size: 20px; white-space: nowrap;
  }
  .card-back .brand-dot { width: 12px; height: 12px; }
  .services {
    position: absolute; left: 232px; top: 30px;
    list-style: none; font-size: 12px; line-height: 15px; color: var(--ink-muted);
  }
  .services li::before { content: "•"; margin-right: 6px; }
  .divider {
    position: absolute; left: 300px; right: 0; top: 176px;
    border-top: 1px solid var(--rule);
  }
  .contact {
    position: absolute; left: 300px; top: 190px;
    list-style: none; font-size: 11.5px; line-height: 15px; color: var(--ink-muted);
  }
  .contact .key { display: inline-block; width: 14px; }
</style>
</head>
<body>
  <main class="sheet">
    <section class="card card-front" aria-label="Card front">
      <div class="brand"><span class="brand-dot"></span>K.R Motor service</div>
    </section>

    <section class="card card-back" aria-label="Card back">
      <ul class="services">
        <li>Oil change</li>
        <li>Scheduled maintenance</li>
        <li>Body Work</li>
        <li>Paint</li>
        <li>Glass Replacement</li>
        <li>NCAB Claims</li>
        <li>Inspections</li>
        <li>Engine repair</li>
      </ul>
      <div class="brand"><span class="brand-dot"></span>K.R Motor service</div>
      <div class="divider"></div>
      <ul class="contact">
        <li><span class="key">A</span>#417-15862 91 Ave, Surrey, BC V5T 8K4</li>
        <li><span class="key">P</span>604 555-0187</li>
        <li><span class="key">F</span>604 555 0142</li>
        <li><span class="key">W</span>www.krmotor.example</li>
      </ul>
    </section>
  </main>
</body>
</html>
```